Renata Quisby

Luxury And Style -

Black - White & Gold

Target Market(s)

Fashion

Industry/Entity Type

Fashion

Requirements
Must have
• High-End
Nice to have
• We will Print on Silk Paper

```html
<!DOCTYPE html>
<html lang="en">
<head>
<meta charset="utf-8">
<title>Renata Quisby Letterhead</title>
<link href="https://fonts.googleapis.com/css2?family=Poppins:wght@300;400;500;600&display=swap" rel="stylesheet">
<style>
  :root {
    --paper: #ffffff;
    --navy: #0f0f26;
    --ink: #ffffff;
    --ink-soft: #e9e8f0;
    --gold: #c59b6a;
    --gold-light: #dcb887;
    --gold-deep: #b48a5a;
  }
  * { margin: 0; padding: 0; box-sizing: border-box; }
  html, body { width: 900px; height: 1200px; overflow: hidden; background: var(--paper); }
  body { font-family: 'Poppins', sans-serif; color: var(--ink); }
  .letterhead {
    position: absolute; left: 40px; top: 20px;
    width: 820px; height: 1160px;
    background: var(--navy); overflow: hidden;
  }
  .brand {
    position: absolute; left: 74px; top: 150px;
    font-weight: 400; font-size: 25px; letter-spacing: 3px;
    color: var(--gold); text-transform: uppercase;
    display: flex; align-items: center; gap: 12px;
  }
  .brand-mark { width: 12px; height: 12px; border-radius: 50%; background: var(--gold); }
  .date { position: absolute; right: 74px; top: 193px; font-size: 12.5px; font-weight: 400; }
  .date strong { font-weight: 500; }
  .addresses { position: absolute; left: 75px; top: 298px; width: 230px; }
  .addr-label { font-size: 14.5px; font-weight: 600; margin-bottom: 14px; }
  .addr-label.name { font-size: 13px; font-weight: 500; margin-bottom: 8px; }
  .addr-lines { font-size: 12.5px; font-weight: 300; line-height: 18px; }
  .addr-block + .addr-block { margin-top: 38px; }
  .letter { position: absolute; left: 338px; top: 278px; width: 408px; }
  .salutation { font-size: 21px; font-weight: 600; margin-bottom: 27px; }
  .letter p {
    font-size: 11.6px; font-weight: 300; line-height: 17.9px;
    text-align: justify; color: var(--ink-soft); margin-left: 2px;
  }
  .letter p + p { margin-top: 32px; }
  .signoff { position: absolute; left: 340px; top: 778px; }
  .signer { font-size: 21.5px; font-weight: 600; line-height: 28px; }
  .role { font-size: 12.5px; font-weight: 300; margin-left: 1px; }
  .signature {
    position: absolute; left: 340px; top: 836px; width: 176px; height: 62px;
    background: linear-gradient(90deg, rgba(255,255,255,0.14), rgba(255,255,255,0.05));
    border-radius: 4px;
  }
  .contacts {
    position: absolute; left: 73px; top: 1055px;
    display: flex; align-items: center;
  }
  .contact { padding-right: 16px; }
  .contact + .contact { padding-left: 16px; border-left: 1.5px solid var(--gold); }
  .contact-label { font-size: 12.5px; font-weight: 500; line-height: 17px; }
  .contact-value { font-size: 11.5px; font-weight: 300; line-height: 17px; }
  .footer-brand {
    position: absolute; right: 74px; top: 1060px;
    font-size: 13px; font-weight: 400; letter-spacing: 1.5px;
    color: var(--gold); text-transform: uppercase;
  }
  .base-band { position: absolute; left: 0; bottom: 0; width: 820px; height: 52px; }
</style>
</head>
<body>
  <main class="letterhead">
    <div class="brand"><span class="brand-mark"></span>Renata Quisby</div>
    <div class="date"><strong>Date:</strong> Octobor 06th, 2025</div>

    <section class="addresses">
      <div class="addr-block">
        <div class="addr-label">To</div>
        <div class="addr-lines">123 Anywhere Address.,<br>Any City, Location Here</div>
      </div>
      <div class="addr-block">
        <div class="addr-label name">Your Name</div>
        <div class="addr-lines">123 Anywhere Address.,<br>Any City, 2nd Location Here</div>
      </div>
    </section>

    <article class="letter">
      <h1 class="salutation">Dear Client</h1>
      <p>Lorem ipsum dolor sit amet, consectetuer adipiscing elit, sed diam nonummy nibh euismod tincidunt ut laoreet dolore magna aliquam erat volutpat. Ut wisi enim ad minim veniam, quis nostrud exerci tation ullamcorper suscipit lobortis nisl ut aliquip ex ea commodo consequat. Duis autem vel eum iriure dolor in hendrerit in vulputate velit esse molestie consequat, vel illum dolore eu feugiat nulla facilisis at vero eros et accumsan et iusto odio dignissim qui blandit praesent luptatum zzril delenit augue duis dolore te feugait nulla facilisi.</p>
      <p>Lorem ipsum dolor sit amet, consectetuer adipiscing elit, sed diam nonummy nibh euismod tincidunt ut laoreet dolore magna aliquam erat volutpat. Ut wisi enim ad minim veniam, quis nostrud exerci tation ullamcorper suscipit lobortis nisl ut aliquip ex ea commodo consequat. Duis autem vel eum iriure dolor in hendrerit in vulputate velit esse molestie consequat,</p>
      <p>Lorem ipsum dolor sit amet, consectetuer adipiscing elit, sed diam nonummy nibh euismod tincidunt ut laoreet dolore magna aliquam erat volutpat.</p>
    </article>

    <div class="signoff">
      <div class="signer">Dorian Pell</div>
      <div class="role">Manager</div>
    </div>
    <div class="signature" role="img" aria-label="Handwritten signature"></div>

    <footer class="contacts">
      <div class="contact"><div class="contact-label">Phone</div><div class="contact-value">+1234 56789</div></div>
      <div class="contact"><div class="contact-label">Email</div><div class="contact-value">www.youremailhere</div></div>
      <div class="contact"><div class="contact-label">Website</div><div class="contact-value">www.yourwebsite.com</div></div>
      <div class="contact"><div class="contact-label">Address</div><div class="contact-value">www.your address here</div></div>
    </footer>
    <div class="footer-brand">Renata Quisby</div>

    <svg class="base-band" viewBox="0 0 820 52" aria-hidden="true">
      <defs>
        <linearGradient id="goldBand" x1="0" y1="0" x2="0" y2="1">
          <stop offset="0" stop-color="var(--gold-deep)"/>
          <stop offset="1" stop-color="var(--gold-light)"/>
        </linearGradient>
      </defs>
      <path d="M0 2 H375 C392 2 398 10 405 19 C410 25 414 27 424 27 H820 V52 H0 Z" fill="url(#goldBand)"/>
      <path d="M0 40 H398 C406 40 410 44 419 52 H0 Z" fill="var(--navy)"/>
    </svg>
  </main>
</body>
</html>
```